Insurance company needs a business card design

We need a business card design for a Massachusetts-based insurance company Cielora Insurance, LLC. We provide auto insurance to Hispanic (Spanish- or Portuguese-speaking) immigrants in the United States. We will give these business cards to auto dealers where such customers typically go to purchase vehicles. We will provide a solution to the dealers to provide easy insurance to the customers buying cars at their dealerships. Cielora is the Spanish word for protection.
Contact Information for Business Card
Name, Designation, Company Name, Address, Phone Number, Email, Website
Look and feel
Each slider illustrates characteristics of the customer's brand and the style your logo design should communicate.

```html
<!DOCTYPE html>
<html lang="en">
<head>
<meta charset="utf-8">
<title>Cielora Insurance – Business Card</title>
<link href="https://fonts.googleapis.com/css2?family=Oswald:wght@500&family=Montserrat:wght@400;500;700&display=swap" rel="stylesheet">
<style>
  :root {
    --page: #d9d9d9;
    --card-blue: #02497c;
    --accent-orange: #f28a0c;
    --text-white: #ffffff;
    --rule: rgba(255,255,255,0.75);
  }
  * { margin: 0; padding: 0; box-sizing: border-box; }
  html, body { width: 1200px; height: 800px; overflow: hidden; }
  body {
    background: var(--page);
    display: flex;
    align-items: center;
    justify-content: center;
    gap: 60px;
    font-family: "Montserrat", sans-serif;
  }
  .card {
    width: 525px;
    height: 300px;
    background: var(--card-blue);
    border-radius: 26px;
    border-bottom: 3px solid var(--accent-orange);
    box-shadow: 0 14px 30px rgba(0,0,0,0.28);
    position: relative;
    overflow: hidden;
  }

  /* Back: contact side */
  .card-back {
    display: flex;
    align-items: center;
    justify-content: center;
    padding-left: 40px;
  }
  .identity {
    text-align: right;
    padding-right: 18px;
  }
  .identity .person-name {
    font-family: "Oswald", sans-serif;
    font-weight: 500;
    font-size: 27px;
    letter-spacing: 0.3px;
    color: var(--accent-orange);
    text-transform: uppercase;
    line-height: 1.05;
  }
  .identity .person-title {
    font-size: 13px;
    color: var(--text-white);
    margin-top: 2px;
  }
  .divider {
    width: 1px;
    height: 118px;
    background: var(--rule);
  }
  .contact-list {
    list-style: none;
    padding-left: 18px;
    color: var(--text-white);
    font-size: 11.5px;
    line-height: 1.5;
  }
  .contact-list .address { margin-bottom: 2px; }
  .contact-list li { display: flex; align-items: center; gap: 8px; }
  .contact-list .icon { width: 11px; height: 11px; flex: none; }
  .contact-list .icon-spacer { width: 11px; flex: none; }

  /* Front: brand side */
  .card-front {
    display: flex;
    align-items: center;
    justify-content: center;
    gap: 16px;
  }
  .brand-dot {
    width: 22px;
    height: 22px;
    border-radius: 50%;
    background: var(--text-white);
  }
  .brand-name {
    font-family: "Montserrat", sans-serif;
    font-weight: 700;
    font-size: 38px;
    letter-spacing: 2px;
    color: var(--text-white);
    text-transform: uppercase;
  }
</style>
</head>
<body>

  <section class="card card-back" aria-label="Business card, contact side">
    <div class="identity">
      <p class="person-name">Daniel Reyes</p>
      <p class="person-title">President</p>
    </div>
    <div class="divider"></div>
    <ul class="contact-list">
      <li class="address"><span class="icon-spacer"></span><span>4218 Harbor View Road<br>Worcester, Mass. 01608</span></li>
      <li>
        <svg class="icon" viewBox="0 0 12 12" aria-hidden="true"><path d="M2.5 1 L4.5 1 L5.2 3.5 L4 4.5 Q5 7 7.5 8 L8.5 6.8 L11 7.5 L11 9.5 Q10.5 11 9 11 Q1 10 1 2.5 Q1 1 2.5 1Z" fill="var(--accent-orange)"/></svg>
        <span>555-014-2273</span>
      </li>
      <li>
        <svg class="icon" viewBox="0 0 12 12" aria-hidden="true"><rect x="3" y="0.5" width="6" height="11" rx="1" fill="none" stroke="var(--accent-orange)" stroke-width="1.2"/><circle cx="6" cy="9.6" r="0.7" fill="var(--accent-orange)"/></svg>
        <span>555-014-8819</span>
      </li>
      <li>
        <svg class="icon" viewBox="0 0 12 12" aria-hidden="true"><rect x="0.5" y="2" width="11" height="8" rx="1" fill="var(--accent-orange)"/><path d="M1 2.8 L6 6.5 L11 2.8" fill="none" stroke="var(--card-blue)" stroke-width="1"/></svg>
        <span>info@cielorainsurance.com</span>
      </li>
      <li>
        <svg class="icon" viewBox="0 0 12 12" aria-hidden="true"><circle cx="6" cy="6" r="5.2" fill="var(--accent-orange)"/><path d="M0.8 6 H11.2 M6 0.8 Q3 6 6 11.2 M6 0.8 Q9 6 6 11.2" fill="none" stroke="var(--card-blue)" stroke-width="0.8"/></svg>
        <span>cielorainsurance.com</span>
      </li>
    </ul>
  </section>

  <section class="card card-front" aria-label="Business card, brand side">
    <span class="brand-dot" aria-hidden="true"></span>
    <p class="brand-name">Cielora Insurance</p>
  </section>

</body>
</html>
```